The Bright Meadow Foundation

This is a non profit . We are a 501(c)(3) charitable organization in the United States. The organization is a volunteer based group providing basic healthcare to those living in underserved rural areas around the world. I have attached a brochure that provides some information about the organization. We are looking for a basic 5 page web page Page 1 Photos that fade into the next x 3 with mission statementPage 2 About us - details about bright meadow foundation. also introducing our Founders of the organization. Marina Kellet, M.D. Dorla Penn , FNP, Rosa Tembley, FNP, Wade Marlow. ( will provide you info on each.Page 3 Projects coming up and futurePage 4 Get involved - Give a donation, Volunteer, Corporate supportPage 5 Support us and contact us with a message box.We mainly work in South America but anticipate trave to South Africa in the near future. Colors bright with emphasis on Reds and Purples. I have attached some photos and ideas. You can use or not use ok to use something similar if you so like

Target Market(s)

People interested in volunteering time or money to overseas medical work. NOT a religious base

Coding

Coded - Design and coding required

Number of Pages Required

1 page

Colors
876aae
ec1f27
f37022
9bcb3c

Requirements
Must have
• Colorful pictures nature, brings out emotion, colorful, children from various parts of the world, animals.
• Tried to down load some pictures but would not go thru.

```html
<!DOCTYPE html>
<html lang="en">
<head>
<meta charset="utf-8">
<title>The Bright Meadow Foundation</title>
<link href="https://fonts.googleapis.com/css2?family=Oswald:wght@400;500;600&family=Lato:ital,wght@0,400;0,700;1,400&display=swap" rel="stylesheet">
<style>
:root{
  --red:#f42a2f;
  --red-deep:#e11d25;
  --purple:#876aae;
  --lilac:#e6dff0;
  --ink:#111;
  --text:#555;
  --grey-band:#efefef;
  --card:#eeeeee;
  --footer:#151515;
  --white:#fff;
}
*{box-sizing:border-box;margin:0;padding:0}
html,body{width:1200px;height:3868px;overflow:hidden}
body{position:relative;background:var(--white);font-family:'Lato',sans-serif;color:var(--text)}
.abs{position:absolute}
.heading{font-family:'Oswald',sans-serif;font-weight:500;color:var(--ink);text-align:center;font-size:46px;line-height:1}

/* top bar */
.topbar{left:0;top:0;width:1200px;height:53px;background:var(--red)}
.topbar .item{top:17px;font-size:12px;color:var(--white);display:flex;align-items:center;gap:14px}
.donate-top{left:942px;top:8px;width:96px;height:37px;background:#0b0b0b;color:#fff;font-size:14px;display:flex;align-items:center;justify-content:center}

/* hero */
.hero{left:0;top:53px;width:1200px;height:600px;border-radius:0 0 44px 44px;overflow:hidden;
  background:linear-gradient(100deg,#2a2c30 0%,#3c3e42 30%,#2f3033 60%,#3a3a3a 85%,#252525 100%)}
.nav{left:0;top:53px;width:1200px;height:67px;background:rgba(0,0,0,.72)}
.brand{left:162px;top:70px;font-family:'Lato',sans-serif;font-weight:700;font-size:20px;color:var(--white);display:flex;align-items:center;gap:10px}
.brand .dot{width:26px;height:26px;border-radius:50%;background:var(--purple)}
.menu{top:78px;font-size:12px;color:var(--white)}
.search{left:987px;top:68px;width:36px;height:36px;border-radius:50%;background:#2a2a2a}
.hero-title{left:0;top:245px;width:1200px;font-family:'Oswald',sans-serif;font-weight:500;font-size:58px;line-height:63px;color:var(--white);text-align:center}
.hero-sub{left:330px;top:402px;width:540px;text-align:center;font-size:13.5px;line-height:21px;color:#eee}
.btn{display:flex;align-items:center;justify-content:center;font-family:'Oswald',sans-serif;font-size:18px}
.btn-solid{background:var(--red);color:var(--white)}
.btn-outline{border:1.5px solid var(--red);color:var(--red)}

/* involvement circles */
.circle{width:240px;height:240px;border-radius:50%;display:flex;flex-direction:column;align-items:center;justify-content:center;gap:18px;font-family:'Oswald',sans-serif;font-size:19px}
.circle.soft{background:var(--lilac);border:1.5px solid var(--purple);color:var(--purple)}
.circle.bold{background:var(--red);color:var(--white);font-weight:500;z-index:2}

/* mission */
.mission{left:0;top:1014px;width:1200px;height:345px;background:var(--grey-band)}
.copy{font-size:12px;line-height:19.5px;text-align:center;color:var(--text)}

/* projects */
.project{width:202px;height:261px;background:var(--card)}
.project .photo{width:202px;height:188px}
.project p{padding:8px 10px 0;font-size:12px;line-height:19.5px;text-align:center;color:#777}

/* partner */
.partner{left:0;top:1862px;width:1200px;height:172px;background:linear-gradient(90deg,#e82a30,#f33a3d 50%,#e5252b)}

/* about */
.about-copy{font-size:12px;line-height:19.5px;color:var(--text)}

/* founders */
.founder{width:361px;height:211px;background:var(--white);box-shadow:0 0 8px rgba(0,0,0,.18)}
.founder p{padding:26px 26px 0 24px;font-style:italic;font-size:12.5px;line-height:21px;color:#666}
.founder-bar{height:83px;background:var(--red);color:var(--white)}
.founder-bar h4{position:absolute;left:32px;top:20px;font-family:'Oswald',sans-serif;font-weight:500;font-size:16px}
.founder-bar span{position:absolute;left:32px;top:48px;font-size:10.5px}
.founder-bar .portrait{position:absolute;right:0;top:0;width:113px;height:83px}
.arrow{width:33px;height:33px;background:var(--purple);display:flex;align-items:center;justify-content:center}

/* contact */
.field{border:1px solid #cfcfcf;background:rgba(255,255,255,.85);font-size:11.5px;color:#666;padding:11px 12px}

/* footer */
.footer{left:0;top:3488px;width:1200px;height:335px;background:var(--footer)}
.foot-h{font-family:'Oswald',sans-serif;font-weight:500;font-size:15px;color:var(--white)}
.foot-h::after{content:"";display:block;width:30px;height:2px;background:var(--red);margin-top:9px}
.links{list-style:none;font-size:11.5px;color:#ddd}
.links li{height:24px;display:flex;align-items:center;gap:9px}
.links li::before{content:"";width:6px;height:6px;border:1.5px solid var(--red);border-radius:50%}
.social{width:36px;height:36px;border-radius:50%;border:1.5px solid #ddd}
.social.on{background:var(--red);border-color:var(--red)}
.info{font-size:11.5px;line-height:14px;color:#eee;display:flex;gap:14px;align-items:flex-start}
.copyright{left:0;top:3823px;width:1200px;height:45px;background:var(--red);color:var(--white);font-size:11px;display:flex;align-items:center;justify-content:center}
</style>
</head>
<body>

<!-- hero -->
<div class="abs hero" role="img" aria-label="Dimmed photograph of a young girl sitting against a wall"></div>
<div class="abs topbar"></div>
<div class="abs topbar item" style="left:494px;width:auto;height:auto;background:none">
  <svg width="20" height="16" viewBox="0 0 24 24"><path fill="#111" d="M6.6 10.8a15 15 0 0 0 6.6 6.6l2.2-2.2c.3-.3.7-.4 1-.2 1.1.4 2.3.6 3.6.6.6 0 1 .4 1 1V20c0 .6-.4 1-1 1A17 17 0 0 1 3 4c0-.6.4-1 1-1h3.5c.6 0 1 .4 1 1 0 1.3.2 2.5.6 3.6.1.3 0 .7-.2 1z"/></svg>
  <span>1-555-014-2290</span>
</div>
<div class="abs topbar item" style="left:658px;width:auto;height:auto;background:none">
  <svg width="20" height="14" viewBox="0 0 20 14"><rect width="20" height="14" rx="1" fill="#111"/><path d="M1 1l9 7 9-7" stroke="#f42a2f" stroke-width="1.5" fill="none"/></svg>
  <span>info@brightmeadowfoundation.org</span>
</div>
<div class="abs donate-top">Donate Now</div>

<div class="abs nav"></div>
<div class="abs brand"><span class="dot"></span>Bright Meadow</div>
<div class="abs menu" style="left:520px">Home</div>
<div class="abs menu" style="left:575px">About us</div>
<div class="abs menu" style="left:646px">Projects</div>
<div class="abs menu" style="left:714px">Get Involved</div>
<div class="abs menu" style="left:805px">Support Us</div>
<div class="abs menu" style="left:888px">Contact Us</div>
<div class="abs search">
  <svg width="36" height="36" viewBox="0 0 36 36"><circle cx="16" cy="16" r="6" stroke="#fff" stroke-width="2.4" fill="none"/><path d="M20.5 20.5l5 5" stroke="#fff" stroke-width="2.6" stroke-linecap="round"/></svg>
</div>

<h1 class="abs hero-title">Give A Helping Hand To Those<br>Who Need It</h1>
<p class="abs hero-sub">Lorem Ipsum is simply dummy text of the printing and typesetting industry. Lorem Ipsum has been the industry's standard dummy text ever since the 1500s.</p>
<div class="abs btn btn-solid" style="left:446px;top:481px;width:128px;height:51px">Give Support</div>
<div class="abs btn btn-outline" style="left:589px;top:481px;width:165px;height:51px">Become Volunteer</div>

<!-- involvement -->
<div class="abs circle soft" style="left:273px;top:712px">
  <svg width="78" height="68" viewBox="0 0 78 68"><rect x="4" y="22" width="70" height="14" fill="#876aae"/><rect x="10" y="38" width="58" height="30" fill="#876aae"/><rect x="34" y="22" width="10" height="46" fill="#e6dff0"/><path d="M39 20c-6-14-20-16-20-6 0 6 12 6 20 6zm0 0c6-14 20-16 20-6 0 6-12 6-20 6z" fill="none" stroke="#876aae" stroke-width="5"/></svg>
  <span>GIVE A DONATION</span>
</div>
<div class="abs circle soft" style="left:685px;top:712px">
  <svg width="78" height="68" viewBox="0 0 78 68"><path d="M50 34c-10-7-16-12-16-19 0-5 4-9 8-9 3 0 6 2 8 5 2-3 5-5 8-5 4 0 8 4 8 9 0 7-6 12-16 19z" fill="#876aae"/><rect x="6" y="38" width="12" height="26" fill="#876aae"/><path d="M20 42h18c4 0 6 3 6 5h12l12-8c3-2 7 1 5 4L58 60H20z" fill="#876aae"/></svg>
  <span>CORPORATE SUPPORT</span>
</div>
<div class="abs circle bold" style="left:478px;top:712px">
  <svg width="78" height="68" viewBox="0 0 78 68"><path d="M39 64C14 46 4 34 4 20 4 10 12 2 22 2c7 0 13 4 17 10 4-6 10-10 17-10 10 0 18 8 18 18 0 14-10 26-35 44z" fill="#fff"/><path d="M22 30l10-9 8 6 10-6 8 8M28 38l8 8M34 34l8 8M40 30l8 8" stroke="#f42a2f" stroke-width="3.5" fill="none" stroke-linecap="round"/></svg>
  <span>BECOME A VOLUNTEER</span>
</div>

<!-- mission -->
<section class="abs mission"></section>
<h2 class="abs heading" style="left:0;top:1064px;width:1200px">Our Mission</h2>
<p class="abs copy" style="left:303px;top:1161px;width:595px">The Bright Meadow Foundation was founded with the aim of helping rural and indigenous individuals in various parts of the world. The Foundation's vision is to see that every woman, man and child have access to basic medical care and treatment as wel l as fundamental knowledge in preventative care.</p>
<p class="abs copy" style="left:303px;top:1239px;width:595px">There are many people living in regions of the world today who have limited or no access to health centers. Often, these individuals travel hours and in many instances days for basic care that often times can be averted with preventative care measures.</p>

<!-- projects -->
<h2 class="abs heading" style="left:0;top:1443px;width:1200px">Our Projects</h2>
<div class="abs project" style="left:162px;top:1544px">
  <div class="photo" role="img" aria-label="Photo of volunteers and young people gathered outdoors" style="background:linear-gradient(180deg,#8fa7c4,#5b6470 55%,#3a3d44)"></div>
  <p>Lorem Ipsum is simply dummy text of the printing and typesetting industry.</p>
</div>
<div class="abs project" style="left:387px;top:1544px">
  <div class="photo" role="img" aria-label="Photo of smiling children lying together on grass" style="background:linear-gradient(160deg,#5f8a3a,#86a85a 45%,#c9b59a 70%,#6f8f45)"></div>
  <p>Lorem Ipsum is simply dummy text of the printing and typesetting industry.</p>
</div>
<div class="abs project" style="left:612px;top:1544px">
  <div class="photo" role="img" aria-label="Photo of a cheerful group of schoolchildren waving" style="background:linear-gradient(180deg,#6d8e4a,#7a5a44 45%,#4a3a32)"></div>
  <p>Lorem Ipsum is simply dummy text of the printing and typesetting industry.</p>
</div>
<div class="abs project" style="left:837px;top:1544px">
  <div class="photo" role="img" aria-label="Photo of a child holding up brightly painted hands" style="background:linear-gradient(135deg,#2f3fb0,#d43ab0 35%,#f3d23a 60%,#3cb35a 80%,#e6e2dc)"></div>
  <p>Lorem Ipsum is simply dummy text of the printing and typesetting industry.</p>
</div>

<!-- partner -->
<section class="abs partner" role="img" aria-label="Red-tinted photo of a crowd of volunteers"></section>
<h2 class="abs heading" style="left:0;top:1882px;width:1200px;font-size:36px">Partner With us</h2>
<p class="abs copy" style="left:370px;top:1942px;width:460px;color:#fff">Creating a more comprehensive medical team of volunteers and resources both from the United States as well other countries and from local communities is a component of the organization's long term goals.</p>

<!-- about -->
<h2 class="abs heading" style="left:162px;top:2138px;text-align:left">About Us</h2>
<p class="abs about-copy" style="left:162px;top:2238px;width:430px">Lorem Ipsum is simply dummy text of the printing and typesetting industry. Lorem Ipsum has been the industry's standard dummy text ever since the 1500s, when an unknown printer took a galley of type and scrambled it to make a type specimen book.</p>
<p class="abs about-copy" style="left:162px;top:2335px;width:430px">It has survived not only five centuries, but also the leap into electronic typesetting, remaining essentially unchanged.</p>
<div class="abs btn btn-solid" style="left:162px;top:2415px;width:96px;height:44px;font-size:15px">Donate Now</div>
<div class="abs" role="img" aria-label="Photo of a smiling little girl hugging a white teddy bear" style="left:668px;top:2103px;width:294px;height:376px;border-radius:46% 46% 40% 40%;background:radial-gradient(ellipse at 50% 35%,#e8c4ae 0%,#d9b29c 30%,#efeaea 60%,#fff 78%)"></div>

<!-- founders -->
<h2 class="abs heading" style="left:0;top:2543px;width:1200px">Our Founder</h2>
<div class="abs arrow" style="left:74px;top:2764px"><svg width="12" height="14" viewBox="0 0 12 14"><path d="M9 1L3 7l6 6" stroke="#fff" stroke-width="1.6" fill="none"/></svg></div>
<div class="abs arrow" style="left:1095px;top:2764px"><svg width="12" height="14" viewBox="0 0 12 14"><path d="M3 1l6 6-6 6" stroke="#fff" stroke-width="1.6" fill="none"/></svg></div>

<div class="abs founder" style="left:161px;top:2673px">
  <p>Dorla Penn is a Nurse Practitioner who is currently practicing in her home state of Colorado. Dorla has spent many years working with underserved populations and has a passion for serving in her global community. Dorla graduated from Northvale State University with a Bachelor's in Nursing.</p>
</div>
<div class="abs founder-bar" style="left:233px;top:2840px;width:356px">
  <h4>DORLA PENN, FNP</h4><span>[Co- Founder]</span>
  <div class="portrait" role="img" aria-label="Portrait photo of Dorla Penn" style="background:linear-gradient(135deg,#c0242a,#7a2a22 50%,#3a1a18)"></div>
</div>

<div class="abs founder" style="left:610px;top:2673px">
  <p>Wade Marlow is a stylist and make-up artist in Boulder ,Colorado. He has always had a passion for helping others. Upon finishing high school, he obtained his Certified Nursing Assistant through Ridgeline Technical College. He worked in a private nursing home for 3 years where hisduties were to care for his patients by feeding,</p>
</div>
<div class="abs founder-bar" style="left:683px;top:2840px;width:355px">
  <h4>WADE MARLOW</h4><span>[Co- Founder]</span>
  <div class="portrait" role="img" aria-label="Portrait photo of Wade Marlow" style="background:linear-gradient(135deg,#e23ad0,#4a3ad8 50%,#2a8ad0)"></div>
</div>

<!-- contact -->
<h2 class="abs heading" style="left:0;top:3008px;width:1200px">Contact Us</h2>
<div class="abs field" style="left:308px;top:3130px;width:281px;height:35px">Name:</div>
<div class="abs field" style="left:611px;top:3130px;width:283px;height:35px">Email:</div>
<div class="abs field" style="left:308px;top:3183px;width:281px;height:35px">Phone:</div>
<div class="abs field" style="left:611px;top:3183px;width:283px;height:35px">Subject:</div>
<div class="abs field" style="left:308px;top:3234px;width:586px;height:88px">Message:</div>
<div class="abs btn btn-solid" style="left:551px;top:3372px;width:96px;height:42px;font-size:15px">Submit Now</div>

<!-- footer -->
<footer class="abs footer"></footer>
<div class="abs brand" style="left:162px;top:3566px;font-size:17px"><span class="dot" style="background:var(--red);width:22px;height:22px"></span>Bright Meadow</div>
<p class="abs" style="left:162px;top:3622px;width:200px;font-size:11.5px;line-height:19.5px;color:#eee">Lorem Ipsum is simply dummy text of the printing and typesetting industry. Lorem Ipsum has been the industry's standard dummy text ever since .</p>
<div class="abs social" style="left:161px;top:3734px"></div>
<div class="abs social" style="left:206px;top:3734px"></div>
<div class="abs social on" style="left:251px;top:3734px"></div>
<div class="abs social" style="left:296px;top:3734px"></div>
<div class="abs social" style="left:339px;top:3734px"></div>

<div class="abs foot-h" style="left:386px;top:3524px">Quick Links</div>
<ul class="abs links" style="left:386px;top:3575px">
  <li>Home</li><li>About us</li><li>Projects</li><li>Get Involved</li><li>Support</li><li>Contact Us</li>
</ul>
<div class="abs foot-h" style="left:613px;top:3524px">Sitemap</div>
<ul class="abs links" style="left:613px;top:3575px">
  <li>Our Volunteer</li><li>Donation</li><li>Support</li><li>Policy</li><li>FAQ</li>
</ul>
<div class="abs foot-h" style="left:837px;top:3524px">Contact Info</div>
<div class="abs info" style="left:835px;top:3582px;font-weight:700">
  <svg width="20" height="18" viewBox="0 0 24 24"><path fill="#f42a2f" d="M6.6 10.8a15 15 0 0 0 6.6 6.6l2.2-2.2c.3-.3.7-.4 1-.2 1.1.4 2.3.6 3.6.6.6 0 1 .4 1 1V20c0 .6-.4 1-1 1A17 17 0 0 1 3 4c0-.6.4-1 1-1h3.5c.6 0 1 .4 1 1 0 1.3.2 2.5.6 3.6.1.3 0 .7-.2 1z"/></svg>
  <span style="padding-top:3px">1-555-014-2290</span>
</div>
<div class="abs info" style="left:837px;top:3623px">
  <svg width="16" height="24" viewBox="0 0 16 24"><path fill="#f42a2f" d="M8 0a8 8 0 0 0-8 8c0 6 8 16 8 16s8-10 8-16a8 8 0 0 0-8-8zm0 11a3 3 0 1 1 0-6 3 3 0 0 1 0 6z"/></svg>
  <span style="padding-left:4px">100- lorem ipsum is simply<br>summy text.</span>
</div>
<div class="abs info" style="left:835px;top:3678px">
  <svg width="20" height="15" viewBox="0 0 20 14"><rect width="20" height="14" rx="1" fill="#f42a2f"/><path d="M1 1l9 7 9-7" stroke="#151515" stroke-width="1.5" fill="none"/></svg>
  <span>info@brightmeadowfound<br>ation.org</span>
</div>

<div class="abs copyright">© 2019. The Bright Meadow Foundation , All Rights Reserved.</div>

</body>
</html>
```